Business IT Services Billboard to attract local small businesses

We are Brivolane, a premier Managed Service Provider (MSP) specializing in comprehensive IT services and VOIP phone solutions exclusively for businesses. Our goal is to create a dynamic and visually engaging billboard advertisement that not only highlights our cutting-edge IT solutions but also emphasizes our state-of-the-art VOIP phone services. This billboard should communicate our commitment to providing innovative, reliable, and holistic technology solutions.
Target Market(s)
small business
Industry/Entity Type
Information Technology
Colors
Designer to choose colors to be used in the design.
Look and feel
Each slider illustrates characteristics of the customer's brand and the style your logo design should communicate.

```html
<!DOCTYPE html>
<html lang="en">
<head>
<meta charset="utf-8">
<title>Brivolane Billboard</title>
<link href="https://fonts.googleapis.com/css2?family=Poppins:wght@400;600;700;800&display=swap" rel="stylesheet">
<style>
  :root {
    --page-bg: #c4c4c4;
    --white: #ffffff;
    --brand-blue: #1a78c2;
    --ink: #1b1b1b;
    --band-dark: #10409a;
    --band-mid: #1a6dbf;
    --band-light: #2a82cf;
    --photo-light: #e3eefb;
    --photo-mid: #8fb8e8;
    --photo-deep: #3f86d2;
  }
  * { margin: 0; padding: 0; box-sizing: border-box; }
  html, body {
    width: 1038px; height: 1200px; overflow: hidden;
    background: var(--page-bg);
    font-family: "Poppins", sans-serif;
  }
  .billboard {
    position: absolute;
    left: 39px; top: 461px;
    width: 960px; height: 278px;
    background: var(--white);
    box-shadow: 0 4px 8px rgba(0,0,0,0.35);
    overflow: hidden;
  }
  .hero-photo {
    position: absolute;
    left: 735px; top: 0;
    width: 225px; height: 172px;
    background:
      radial-gradient(ellipse at 70% 55%, var(--photo-deep) 0%, transparent 60%),
      linear-gradient(90deg, var(--white) 0%, var(--photo-light) 22%, var(--photo-mid) 60%, var(--photo-deep) 100%);
  }
  .brand-name {
    position: absolute;
    left: 26px; top: 62px;
    width: 150px;
    font-weight: 800;
    font-size: 31px;
    color: var(--brand-blue);
    letter-spacing: -0.5px;
  }
  .headline {
    position: absolute;
    left: 205px; top: 24px;
  }
  .headline-kicker {
    display: block;
    font-weight: 600;
    font-size: 20px;
    letter-spacing: 6.2px;
    color: var(--ink);
    line-height: 1;
  }
  .headline-main {
    display: block;
    margin-top: 6px;
    font-weight: 700;
    font-size: 61px;
    letter-spacing: -2.5px;
    color: var(--brand-blue);
    line-height: 1;
  }
  .headline-sub {
    display: block;
    margin-top: 2px;
    font-weight: 800;
    font-size: 52px;
    letter-spacing: 5px;
    color: var(--ink);
    line-height: 1;
  }
  .tagline-band {
    position: absolute;
    left: 0; top: 172px;
    width: 100%; height: 43px;
    background: var(--band-dark);
    color: var(--white);
    font-weight: 700;
    font-size: 21.5px;
    line-height: 43px;
    padding-left: 26px;
    white-space: nowrap;
  }
  .cta-band {
    position: absolute;
    left: 0; top: 215px;
    width: 100%; height: 63px;
    background: linear-gradient(90deg, var(--band-mid), var(--band-light) 50%, var(--band-mid));
    color: var(--white);
    display: flex;
    align-items: center;
    justify-content: space-between;
    padding: 0 32px 6px 26px;
  }
  .cta-lead {
    font-weight: 400;
    font-size: 21.5px;
  }
  .cta-url {
    font-weight: 700;
    font-size: 31px;
    letter-spacing: 5px;
  }
</style>
</head>
<body>
  <div class="billboard">
    <div class="hero-photo" role="img" aria-label="Photo of a businessman working at a laptop with blue technology graphics"></div>
    <div class="brand-name">Brivolane</div>
    <h1 class="headline">
      <span class="headline-kicker">ELEVATE YOUR BUSINESS WITH</span>
      <span class="headline-main">NEXT-GEN IT &amp;</span>
      <span class="headline-sub">VOIP SERVICES</span>
    </h1>
    <div class="tagline-band">Innovative IT and VOIP Solutions Tailored for Your Business Success</div>
    <div class="cta-band">
      <span class="cta-lead">Transform Your Tech Today at</span>
      <span class="cta-url">www.brivolane.com</span>
    </div>
  </div>
</body>
</html>
```